Tindalee Pure Honey

Dear Friends I would like a label to designed for a new brand we wish to create called TINDALEE pure honey.

I need 2 versions

Version 1 - normal general version for every buyer

Version 2 - this is a KIDS HONEY version and must be designed
specifically to attract Kids and be fun.

Version 1 size is 127mm wide x 60mm high

Version 2 size is 168mm long x 60mm wide

labels must be set up with following info on the face of the product

TINDALEE

100% Pure Honey

AUSTRALIAN

For version 2 we must have the words KIDS HONEY on the face.

Best regards

Selim

Product

• Please note the label layout is landscape so 127mm wide x 60mm high

```html
<!DOCTYPE html>
<html lang="en">
<head>
<meta charset="utf-8">
<title>Tindalee Pure Honey – Label</title>
<link rel="stylesheet" href="https://fonts.googleapis.com/css2?family=Della+Respira&family=Open+Sans:wght@500;700&display=swap">
<style>
  :root {
    --amber-core: #f9a526;
    --amber-mid: #f2841f;
    --amber-edge: #df5a1e;
    --shield-rim: #c9481a;
    --gold-line: #f8c27e;
    --cream: #fbe3b8;
    --white: #ffffff;
    --ink: #111111;
  }
  html, body {
    margin: 0;
    padding: 0;
    width: 1200px;
    height: 567px;
    overflow: hidden;
    background: #ffffff;
  }
  .label {
    position: relative;
    width: 1200px;
    height: 567px;
    overflow: hidden;
    background: radial-gradient(ellipse 620px 420px at 600px 283px, var(--amber-core) 0%, var(--amber-mid) 45%, var(--amber-edge) 100%);
  }
  .label h1, .label p { margin: 0; }
  .label__band {
    position: absolute;
    left: 0;
    width: 1200px;
    height: 11px;
    background: linear-gradient(90deg, #f9b777 0%, #fcc98f 50%, #f9b777 100%);
  }
  .label__band--top { top: 14px; }
  .label__band--bottom { top: 541px; }
  .shield {
    position: absolute;
    left: 0;
    top: 0;
  }
  .brand-name {
    position: absolute;
    left: 0;
    width: 1200px;
    top: 128px;
    text-align: center;
    font-family: "Della Respira", serif;
    font-weight: 400;
    font-size: 80px;
    line-height: 1;
    letter-spacing: 2px;
    color: var(--gold-line);
    text-shadow: 0 2px 4px rgba(120, 40, 0, 0.35);
  }
  .brand-product {
    position: absolute;
    left: 0;
    width: 1200px;
    top: 200px;
    text-align: center;
    font-family: "Della Respira", serif;
    font-size: 40px;
    line-height: 1;
    color: var(--cream);
  }
  .origin {
    position: absolute;
    left: 0;
    width: 1200px;
    top: 431px;
    text-align: center;
    font-family: "Open Sans", sans-serif;
    font-weight: 500;
    font-size: 22px;
    line-height: 1.2;
    color: var(--white);
  }
  .net-weight {
    position: absolute;
    left: 118px;
    top: 470px;
    font-family: "Della Respira", serif;
    font-size: 32px;
    line-height: 1.2;
    color: var(--ink);
  }
  .net-weight__mark {
    font-family: "Open Sans", sans-serif;
    font-weight: 700;
    font-size: 36px;
    margin-right: 8px;
  }
  .purity {
    position: absolute;
    left: 756px;
    top: 487px;
    font-family: "Della Respira", serif;
    font-size: 27px;
    line-height: 1.2;
    color: var(--cream);
  }
</style>
</head>
<body>
<main class="label">
  <div class="label__band label__band--top"></div>
  <div class="label__band label__band--bottom"></div>

  <svg class="shield" width="1200" height="567" viewBox="0 0 1200 567">
    <defs>
      <radialGradient id="shieldFill" cx="600" cy="300" r="300" gradientUnits="userSpaceOnUse">
        <stop offset="0" stop-color="#f8a524"/>
        <stop offset="0.5" stop-color="#ee6f1f"/>
        <stop offset="1" stop-color="#d9561c"/>
      </radialGradient>
      <radialGradient id="cellGlow" cx="598" cy="345" r="130" gradientUnits="userSpaceOnUse">
        <stop offset="0" stop-color="#fbb22a"/>
        <stop offset="1" stop-color="#f07a22" stop-opacity="0"/>
      </radialGradient>
    </defs>
    <path class="shield__outer"
      d="M364,134 Q600,64 836,134 L836,412 Q762,414 758,450 L758,474 Q758,518 704,518 L496,518 Q442,518 442,474 L442,450 Q438,414 364,412 Z"
      fill="var(--shield-rim)"/>
    <path class="shield__body"
      d="M372,140 Q600,74 828,140 L828,404 Q752,408 750,446 L750,472 Q750,510 702,510 L498,510 Q450,510 450,472 L450,446 Q448,408 372,404 Z"
      fill="url(#shieldFill)"/>
    <path class="shield__rule"
      d="M380,150 Q600,86 820,150 L820,396 Q744,400 740,442 L740,468 Q740,500 700,500 L500,500 Q460,500 460,468 L460,442 Q456,400 380,396 Z"
      fill="none" stroke="var(--gold-line)" stroke-width="3"/>
    <rect class="honeycomb-area" role="img" aria-label="Honeycomb cells emblem"
      x="472" y="280" width="254" height="132" rx="20" fill="url(#cellGlow)"/>
  </svg>

  <h1 class="brand-name">Tindalee</h1>
  <p class="brand-product">honey</p>
  <p class="origin">AUSTRALIAN</p>
  <p class="net-weight"><span class="net-weight__mark">e</span>750 gr</p>
  <p class="purity">100% Pure Honey</p>
</main>
</body>
</html>
```